Restaurant Facility Equipment & Store Maintenance/

I need a flyer showing commercial/industrial kitchen equipment photos we work on Hot Equipment & Cold Equipment and offer many services. see attached highlights

```html
<!DOCTYPE html>
<html lang="en">
<head>
<meta charset="UTF-8">
<title>Restaurant Facility Equipment & Store Maintenance</title>
<link rel="stylesheet" href="https://fonts.googleapis.com/css2?family=Poppins:ital,wght@0,800;1,300;1,400;1,700&display=swap">
<style>
  :root {
    --yellow: #ffc800;
    --dark: #151515;
    --ink: #111111;
    --white: #ffffff;
    --cream: #f4e7b8;
  }
  html, body { margin: 0; padding: 0; overflow: hidden; }
  body { width: 927px; height: 1200px; background: var(--white); }
  .flyer {
    position: relative;
    width: 927px; height: 1200px;
    overflow: hidden;
    font-family: "Poppins", sans-serif;
    background: var(--white);
  }
  .kitchen-backdrop {
    position: absolute; left: 0; top: 0; width: 927px; height: 719px;
    background: radial-gradient(ellipse at 35% 40%, #3a3a3a 0%, #222 45%, var(--dark) 100%);
  }
  .shapes { position: absolute; left: 0; top: 0; }
  .headline {
    position: absolute; left: 36px; top: 62px; margin: 0;
    color: var(--white);
    font-weight: 800; font-size: 30.5px; line-height: 38px;
    letter-spacing: -0.2px; text-transform: uppercase;
  }
  .intro {
    position: absolute; left: 39px; top: 229px; margin: 0;
    color: var(--cream);
    font-style: italic; font-weight: 300;
    font-size: 21px; line-height: 29.5px;
  }
  .intro .motto { color: var(--yellow); font-weight: 700; }
  .services-title {
    position: absolute; left: 40px; top: 484px; margin: 0;
    color: var(--white);
    font-weight: 800; font-size: 30px; letter-spacing: -0.5px;
    text-shadow: 2px 2px 3px rgba(0,0,0,0.35);
  }
  .services-list {
    position: absolute; left: 49px; top: 543px; width: 545px;
    margin: 0; padding: 0 0 0 18px;
    color: var(--ink);
    font-style: italic; font-weight: 400;
    font-size: 18.4px; line-height: 29.5px;
  }
  .services-list li::marker { font-size: 12px; }
  .services-list .emphasis { font-weight: 700; }
  .photo {
    position: absolute; left: 675px; width: 209px; height: 283px;
  }
  .photo-mixer { top: 3px; background: linear-gradient(160deg, #5a6266, #2b3235 60%, #1c2224); }
  .photo-chef { top: 307px; background: linear-gradient(170deg, #cfd2d4, #8d9396 55%, #4b4f52); }
  .photo-line { top: 610px; background: linear-gradient(165deg, #e2e4e5, #b5babd 50%, #7d8387); }
  .photo-range { top: 914px; background: linear-gradient(170deg, #c9cccd, #8a8f92 55%, #505456); }
</style>
</head>
<body>
<main class="flyer">
  <div class="kitchen-backdrop" role="img" aria-label="Dimly lit commercial kitchen with stainless steel equipment"></div>

  <svg class="shapes" width="927" height="1200" viewBox="0 0 927 1200" aria-hidden="true">
    <rect x="903" y="719" width="24" height="481" fill="var(--white)"/>
    <rect x="656" y="0" width="247" height="1200" fill="var(--yellow)"/>
    <polygon points="0,464 593,464 656,834 594,1200 0,1200" fill="var(--yellow)"/>
    <g fill="var(--yellow)">
      <polygon points="369,0 404,0 436,28 436,51"/>
      <polygon points="432,0 467,0 499,28 499,51"/>
      <polygon points="495,0 530,0 562,28 562,51"/>
    </g>
    <g fill="var(--ink)">
      <polygon points="108,1200 155,1164 155,1200"/>
      <polygon points="154,1200 200,1164 200,1200"/>
      <polygon points="199,1200 246,1164 246,1200"/>
    </g>
  </svg>

  <h1 class="headline">Installation, Rebuilds, OSHA<br>Inspection, and Preventive<br>Maintenance Services for Denver<br>Metro and Surrounding Areas.</h1>

  <p class="intro"><span class="motto">"We handle everything from the front door to the<br>back door."</span> We offer hot and cold equipment repair,<br>cleaning, maintenance, handyman work, drywall,<br>painting, door closers, floors, and ceiling tiles. For any<br>need in your restaurant, call us and we will send a<br>skilled technician to manage all your commercial and<br>industrial facility requirements.</p>

  <h2 class="services-title">OUR SERVICES:</h2>

  <ul class="services-list">
    <li>NKSA Certified Technicians</li>
    <li>Round-the-clock emergency services</li>
    <li>Customers who subscribe to preventive maintenance services receive a reduced rate on hourly labor charges.</li>
    <li class="emphasis">Original equipment manufacturer (OEM) parts</li>
    <li>30-day warranty on all OEM parts installed</li>
    <li>Equipment Cleaning &amp; Rebuilds</li>
    <li>Used equipment available for purchase or rental</li>
    <li>Specialized Programs for Preventive Maintenance of Equipment</li>
    <li>Installation and Repair of Restaurant Equipment</li>
    <li>Repair or replace restaurant furniture</li>
    <li>Comprehensive licensed electrical contractor services for both interior and exterior projects, including lighting system upgrades.</li>
    <li>Building Graffiti Removal Services</li>
    <li>Hot &amp; Cold Equipment</li>
    <li>Food Service Trucks</li>
    <li>We repair floors, walls, counters, décor, signage, parking lots, dumpsters, and more. If you have it, we probably fix it.</li>
  </ul>

  <div class="photo photo-mixer" role="img" aria-label="Commercial stand mixer with steel bowl and safety guard"></div>
  <div class="photo photo-chef" role="img" aria-label="Cook straining sauce at a stainless steel kitchen line"></div>
  <div class="photo photo-line" role="img" aria-label="Clean stainless steel cooking line under an exhaust hood"></div>
  <div class="photo photo-range" role="img" aria-label="Gas range with steel pots and pans"></div>
</main>
</body>
</html>
```